Prepare a modern, professional business card for Meridel Vantage Advisory (MVA) Our company is in the banking, compliance and finance industry. We provide kiosks, software integration, and compliance guidelines so that banks can "bank" Marijuana Dispensaries with MonLex, Office of Statute Review and NBRA approval.

Target Market(s)

Banks

Industry/Entity Type

Business

Contact Information for Business Card

Peter L Oakridge
Meridel Vantage Advisory
Vice President
4427 Larkspur Crossing Way
Suite 218
Las Vegas, NV 89135
pete@mvalq.com
555-418-7362

Font styles to use
Sans Serif

Requirements
Nice to have
• I like the clean simple appearance of Quince computers. Perhaps the three LETTERS of MVA can be the LOGO on the Card and the Company name could be incorporated in the contact information. Like colors of white, black and gray

```html
<!DOCTYPE html>
<html lang="en">
<head>
<meta charset="utf-8">
<title>Meridel Vantage Advisory – Business Card</title>
<link href="https://fonts.googleapis.com/css2?family=Saira:wght@400&display=swap" rel="stylesheet">
<style>
  :root {
    --backdrop: #d6d6d6;
    --card: #0e0e0e;
    --white: #ffffff;
    --gray: #7b7b7b;
    --gray-soft: #8f8f8f;
    --rule: #666666;
  }
  * { margin: 0; padding: 0; box-sizing: border-box; }
  html, body {
    width: 1200px;
    height: 900px;
    overflow: hidden;
    background: var(--backdrop);
    font-family: "Saira", Arial, sans-serif;
    font-weight: 400;
  }
  .business-card {
    position: absolute;
    left: 100px;
    top: 164px;
    width: 1000px;
    height: 572px;
    background: var(--card);
    box-shadow: 0 10px 30px rgba(0,0,0,0.25);
  }
  .brand-mark {
    position: absolute;
    left: 64px;
    top: 112px;
    font-size: 118px;
    line-height: 1;
    letter-spacing: 4px;
    color: var(--gray);
  }
  .rule { position: absolute; height: 1px; background: var(--rule); }
  .rule-upper { left: 430px; right: 40px; top: 222px; }
  .rule-lower { left: 200px; width: 560px; top: 356px; }
  .holder-name {
    position: absolute;
    left: 470px;
    top: 232px;
    font-size: 28px;
    letter-spacing: 1px;
    color: var(--white);
    text-transform: uppercase;
  }
  .holder-title {
    position: absolute;
    left: 600px;
    top: 276px;
    font-size: 17px;
    color: var(--gray);
  }
  .company-name {
    position: absolute;
    left: 400px;
    top: 310px;
    font-size: 26px;
    letter-spacing: 1px;
    color: var(--white);
    text-transform: uppercase;
  }
  .address {
    position: absolute;
    left: 200px;
    top: 366px;
    font-size: 25px;
    letter-spacing: 0.5px;
    color: var(--gray);
    white-space: nowrap;
  }
  .contact-line {
    position: absolute;
    left: 330px;
    top: 414px;
    display: flex;
    align-items: center;
    gap: 14px;
    font-size: 24px;
    color: var(--gray-soft);
  }
  .bullet {
    width: 15px;
    height: 15px;
    background: var(--white);
    display: inline-block;
  }
  .contact-item { margin-right: 14px; }
</style>
</head>
<body>
  <div class="business-card">
    <div class="brand-mark">MVA</div>
    <div class="rule rule-upper"></div>
    <div class="holder-name">Peter L Oakridge</div>
    <div class="holder-title">Vice President</div>
    <div class="company-name">Meridel Vantage Advisory</div>
    <div class="rule rule-lower"></div>
    <div class="address">4427 Larkspur Crossing Way Suite 218 Las Vegas, NV 89135</div>
    <div class="contact-line">
      <span class="bullet"></span>
      <span class="contact-item">pete@mvalq.com</span>
      <span class="bullet"></span>
      <span class="contact-item">555-418-7362</span>
      <span class="bullet"></span>
    </div>
  </div>
</body>
</html>
```